Dorrish Electric Ltd

Looking for a single page website and Facebook page design. I am an electrical contractor based on Vancouver Island. I do service, custom homes, residential and commercial installations. My company just started out, so I don't have any pictures of installs yet. I have 25 years experience. I would like the colors to be my logo colors black and I have a black Corvan Ridgeback that will be my vehicle which I will have a wrap for.
Updates

I just posted the contest today, not sure why the deadline is the same day.

Went on vacation/holiday

Industry/Entity Type

Electrician

Requirements
Must have
• Services provided, About me section, quote section,
Nice to have
• I am not quite sure yet, I need to see some designs first .

```html
<!DOCTYPE html>
<html lang="en">
<head>
<meta charset="utf-8">
<title>Dorrish Electric Ltd</title>
<link href="https://fonts.googleapis.com/css2?family=Oswald:wght@500&family=Roboto:ital,wght@0,400;0,500;0,700;1,400&family=Syncopate:wght@700&display=swap" rel="stylesheet">
<style>
:root{
  --yellow:#f4b400;
  --yellow-deep:#e7a800;
  --ink:#111111;
  --dark:#161616;
  --text:#444444;
  --muted:#6a6a6a;
  --light:#f4f5f7;
  --white:#ffffff;
}
*{margin:0;padding:0;box-sizing:border-box}
html,body{width:1200px;height:4170px;overflow:hidden}
body{position:relative;font-family:"Roboto",sans-serif;color:var(--text);background:var(--white)}
.abs{position:absolute}
.display{font-family:"Syncopate",sans-serif;font-weight:700;text-transform:uppercase;letter-spacing:1px}
.btn{position:absolute;display:flex;align-items:center;justify-content:center;font-size:14px;font-weight:700;text-transform:uppercase;color:var(--white);background:var(--yellow)}
.btn-outline{background:transparent;border:1.5px solid var(--white)}
.eyebrow{position:absolute;left:0;width:1200px;text-align:center;color:var(--yellow);font-size:17px;text-transform:uppercase}
.section-title{position:absolute;left:0;width:1200px;text-align:center;font-size:32px;color:var(--ink)}

/* header */
.header{position:absolute;left:0;top:0;width:1200px;height:95px;background:var(--white);border-top:3px solid var(--yellow)}
.brand{position:absolute;left:98px;top:16px;display:flex;align-items:center;gap:10px}
.brand-dot{width:56px;height:56px;border-radius:50%;border:3px solid var(--ink)}
.brand-name{font-size:13px;font-weight:700;color:var(--ink);text-transform:uppercase}
.topbar{position:absolute;top:0;height:40px}
.topbar-call{left:560px;width:240px}
.topbar-mail{left:785px;width:320px}
.topbar span{position:absolute;top:12px;font-size:13px;color:var(--white)}
.nav{position:absolute;top:63px;left:512px;display:flex;gap:0;font-size:14px;color:var(--ink);text-transform:uppercase}
.nav a{position:absolute;white-space:nowrap;color:inherit;text-decoration:none}

/* hero */
.hero-text{left:102px;color:var(--white)}

/* about */
.about-para{position:absolute;left:640px;top:980px;width:460px;font-size:13.5px;line-height:27px;color:var(--text)}

/* split */
.split-head{position:absolute;top:1427px;font-size:27px;color:var(--white)}
.split-para{position:absolute;top:1478px;width:400px;font-size:14px;line-height:25px;color:var(--white)}

/* projects */
.project{position:absolute;width:235px;height:300px;background:var(--white);box-shadow:0 2px 8px rgba(0,0,0,.18);padding:5px}
.project .photo{width:225px;height:250px}
.project .caption{position:absolute;left:5px;right:5px;bottom:5px;height:40px;background:var(--yellow);color:var(--white);font-size:18px;font-weight:700;display:flex;align-items:center;justify-content:center}
.arrow{position:absolute;width:32px;height:32px;border-radius:50%;border:1.5px solid #777}

/* reviews */
.review{position:absolute;top:2640px;width:330px}
.avatar{position:absolute;left:0;top:0;width:58px;height:58px;border-radius:50%;background:linear-gradient(#cfcfcf,#8d8d8d);border:3px solid var(--white);box-shadow:0 1px 4px rgba(0,0,0,.2)}
.quote-mark{position:absolute;left:66px;top:-6px;font-size:34px;color:var(--yellow);font-family:"Oswald",sans-serif}
.review p{position:absolute;left:90px;top:0;width:240px;font-size:11px;font-style:italic;line-height:21px;color:var(--muted)}
.review .name{position:absolute;left:90px;top:92px;font-size:12px;color:var(--ink)}
.review .stars{position:absolute;left:90px;top:112px;font-size:15px;color:var(--yellow);letter-spacing:1px}

/* news */
.news{position:absolute;top:3040px;width:320px;height:438px;background:var(--white);box-shadow:0 1px 6px rgba(0,0,0,.14)}
.news .photo{width:320px;height:218px}
.news .date{position:absolute;left:14px;top:244px;font-size:12px;color:var(--muted)}
.news h3{position:absolute;left:14px;top:268px;width:300px;font-size:21px;font-weight:500;line-height:26px;color:var(--ink)}
.news p{position:absolute;left:14px;top:334px;width:295px;font-size:12px;line-height:21px;color:var(--muted)}
.news .more{position:absolute;left:14px;top:405px;font-size:12.5px;font-weight:700;color:var(--yellow);text-decoration:underline}

/* footer */
.footer-title{position:absolute;left:125px;top:3790px;font-size:18px;color:var(--white)}
.field{position:absolute;left:125px;width:478px;height:40px;background:var(--white);font-size:13px;color:#555;padding:12px 16px}
.foot-head{position:absolute;left:730px;font-size:14px;font-weight:700;color:var(--white);text-transform:uppercase}
.foot-text{position:absolute;left:730px;font-size:14px;line-height:27px;color:var(--white)}
.social{position:absolute;top:4030px;width:20px;height:20px;border-radius:50%;background:var(--white)}
</style>
</head>
<body>

<!-- header -->
<header class="header">
  <div class="brand"><div class="brand-dot"></div><div class="brand-name">Dorrish Electric Ltd</div></div>
  <svg class="topbar topbar-call" viewBox="0 0 240 40" width="240" height="40" style="position:absolute;left:560px;top:0"><polygon points="22,0 240,0 218,40 0,40" fill="#f4b400"/><circle cx="35" cy="20" r="10" fill="none" stroke="#fff" stroke-width="1.5"/><path d="M31 15l3 0 1 3-2 1.5a8 8 0 0 0 3 3l1.5-2 3 1v3a1 1 0 0 1-1 1 12 12 0 0 1-9.5-9.5 1 1 0 0 1 1-1z" fill="#fff"/></svg>
  <svg viewBox="0 0 320 40" width="320" height="40" style="position:absolute;left:785px;top:0"><polygon points="22,0 320,0 298,40 0,40" fill="#111"/><circle cx="40" cy="20" r="11" fill="#fff"/><rect x="34" y="15" width="12" height="9" fill="#111"/><path d="M34 15l6 5 6-5" stroke="#fff" stroke-width="1.2" fill="none"/></svg>
  <span class="abs" style="left:615px;top:12px;font-size:13px;color:#fff">Call Us : (555) 014-2290</span>
  <span class="abs" style="left:847px;top:12px;font-size:13px;color:#fff">Mail Us : info@dorrishelectric.example</span>
  <nav class="nav" style="left:0;width:1200px">
    <a style="left:512px;color:var(--yellow)">Home</a>
    <a style="left:596px">About Us</a>
    <a style="left:708px">Services</a>
    <a style="left:817px">Projects</a>
    <a style="left:932px">Blog</a>
    <a style="left:1010px">Contact Us</a>
  </nav>
</header>

<!-- hero -->
<section>
  <div class="abs" role="img" aria-label="Smiling electrician in hard hat and safety vest on a yellow ladder wiring a ceiling unit" style="left:0;top:95px;width:1200px;height:620px;background:linear-gradient(100deg,#3a3b3d 0%,#6c6e72 45%,#9a9b9c 70%,#5d5e60 100%)"></div>
  <svg class="abs" style="left:0;top:590px" width="1200" height="140" viewBox="0 0 1200 140">
    <path d="M0 25 Q600 190 1200 25 L1200 140 L0 140 Z" fill="#f7f7f7"/>
    <path d="M0 25 Q600 190 1200 25" fill="none" stroke="#f4b400" stroke-width="5"/>
  </svg>
  <svg class="abs" style="left:62px;top:337px" width="20" height="40"><path d="M16 2 L4 20 L16 38" stroke="#fff" stroke-width="2" fill="none"/></svg>
  <svg class="abs" style="left:1118px;top:337px" width="20" height="40"><path d="M4 2 L16 20 L4 38" stroke="#fff" stroke-width="2" fill="none"/></svg>
  <div class="abs hero-text" style="top:277px;font-size:18px">DORRISH ELECTRIC LTD</div>
  <div class="abs hero-text display" style="top:318px;font-size:29px;line-height:36px">Quality, Excellence,<br>and Reliability</div>
  <div class="btn" style="left:100px;top:420px;width:180px;height:47px">Schedule Service</div>
</section>

<!-- about -->
<section>
  <div class="abs" style="left:0;top:715px;width:1200px;height:607px;background:linear-gradient(90deg,#fbfbfb,#f1f2f3)"></div>
  <div class="abs" style="left:110px;top:780px;width:460px;height:460px;border-radius:50%;border:6px solid var(--yellow);background:var(--white)"></div>
  <div class="abs" role="img" aria-label="Portrait of a smiling electrician in an orange hard hat holding a cable" style="left:140px;top:810px;width:400px;height:400px;border-radius:50%;background:radial-gradient(circle at 50% 40%,#4a7fc7,#1c3f8a)"></div>
  <div class="abs" style="left:640px;top:817px;font-size:17px;color:var(--yellow)">ABOUT ME</div>
  <div class="abs" style="left:640px;top:840px;font-family:'Oswald',sans-serif;font-weight:500;font-size:44px;color:var(--ink)">DORRISH ELECTRIC LTD</div>
  <div class="abs" style="left:640px;top:903px;width:480px;font-size:24px;font-weight:500;line-height:32px;color:var(--ink)">Outstanding Commercial and Residential Electrical Services</div>
  <p class="about-para">At vero eos et accusamus et iusto odio dignissimos ducimus qui blanditiis praesentium voluptatum deleniti atque pti quos dolores et quas molestias excepturi sint occaidtate non provident, similique sunt in culpa qui officia deserunt mollitia animi, id est laborum et m fuga. Et harum quidem rerum facilis est et expedita distinctio. Nam libero tempore, cum soluta nobis est eligendi optio cumque nihil impedit</p>
  <div class="btn" style="left:640px;top:1165px;width:175px;height:47px">Learn More</div>
</section>

<!-- services split -->
<section>
  <div class="abs" role="img" aria-label="Residential house at dusk" style="left:0;top:1322px;width:1200px;height:488px;background:linear-gradient(90deg,#2a2a2a,#141414)"></div>
  <svg class="abs" style="left:0;top:1322px" width="1200" height="488"><polygon points="0,0 530,0 652,488 0,488" fill="#f0b70d"/></svg>
  <div class="abs" style="left:554px;top:1520px;width:94px;height:94px;border-radius:50%;background:var(--white);border:5px solid #e0e0e0"></div>
  <div class="abs" style="left:574px;top:1540px;width:54px;height:54px;border-radius:50%;border:3px solid var(--ink)"></div>
  <div class="split-head display" style="left:100px">For Commercial</div>
  <p class="split-para" style="left:100px">Lorem ipsum dolor sit amet, consectetur adipiscing elit, sed do eiusmod tempor incididunt ut labore et dolore magna ala. Quis ipsum suspendisse ultrida. Risus commodo viverra maecenas accumsan lacus vel facilisim ipsum dolor sit amet, consectetur adipiscing elit, sed do eiusmod tempor incididunt ut labore et dolore magna ala.</p>
  <div class="btn btn-outline" style="left:100px;top:1653px;width:174px;height:47px">Learn More</div>
  <div class="split-head display" style="left:700px">For Residential</div>
  <p class="split-para" style="left:700px">Lorem ipsum dolor sit amet, consectetur adipiscing elit, sed do eiusmod tempor incididunt ut labore et dolore magna ala. Quis ipsum suspendisse ultrida. Risus commodo viverra maecenas accumsan lacus vel facilisim ipsum dolor sit amet, consectetur adipiscing elit, sed do eiusmod tempor incididunt ut labore et dolore magna ala.</p>
  <div class="btn btn-outline" style="left:700px;top:1653px;width:174px;height:47px">Learn More</div>
</section>

<!-- projects -->
<section>
  <div class="abs" style="left:0;top:1810px;width:1200px;height:620px;background:linear-gradient(#f2f2f2,#fbfbfb)"></div>
  <div class="eyebrow" style="top:1900px">Latest Works</div>
  <div class="section-title display" style="top:1933px">Past Projects</div>
  <div class="arrow" style="left:52px;top:2156px"></div>
  <div class="arrow" style="left:1117px;top:2156px"></div>
  <div class="project" style="left:100px;top:2010px"><div class="photo" role="img" aria-label="Electrician on a ladder in a timber-framed building" style="background:linear-gradient(#c69a6a,#7a5a3c)"></div><div class="caption">Finibus Bonorum et</div></div>
  <div class="project" style="left:355px;top:2035px"><div class="photo" role="img" aria-label="Electrician pulling wires by a brick wall" style="background:linear-gradient(#a86a4a,#5b4a4a)"></div><div class="caption">Finibus Bonorum et</div></div>
  <div class="project" style="left:610px;top:2010px"><div class="photo" role="img" aria-label="Electrician working on a breaker panel" style="background:linear-gradient(#9a9ea3,#4e5257)"></div><div class="caption">Finibus Bonorum et</div></div>
  <div class="project" style="left:865px;top:2035px"><div class="photo" role="img" aria-label="Technician checking an outdoor electrical unit under a blue sky" style="background:linear-gradient(#3a78c8,#a7b3bd)"></div><div class="caption">Finibus Bonorum et</div></div>
</section>

<!-- reviews -->
<section>
  <div class="abs" style="left:0;top:2430px;width:1200px;height:440px;background:var(--light)"></div>
  <div class="eyebrow" style="top:2520px">Testimoinals</div>
  <div class="section-title display" style="top:2552px">Customer Reviews</div>
  <div class="arrow" style="left:52px;top:2685px"></div>
  <div class="arrow" style="left:1117px;top:2685px"></div>
  <div class="review" style="left:105px"><div class="avatar" role="img" aria-label="Customer portrait"></div><span class="quote-mark">“</span><p>At vero eos et accusao odio dignissimos ducimus quditiis praesentium voluptatum deleniti atque corrupti quos dolores et quas molestias excepturi sint</p><div class="name">- RAVI T.</div><div class="stars">★★★★★</div></div>
  <div class="review" style="left:450px"><div class="avatar" role="img" aria-label="Customer portrait"></div><span class="quote-mark">“</span><p>At vero eos et accusao odio dignissimos ducimus quditiis praesentium voluptatum deleniti atque corrupti quos dolores et quas molestias excepturi sint</p><div class="name">- OWEN P.</div><div class="stars">★★★★★</div></div>
  <div class="review" style="left:795px"><div class="avatar" role="img" aria-label="Customer portrait"></div><span class="quote-mark">“</span><p>At vero eos et accusao odio dignissimos ducimus quditiis praesentium voluptatum deleniti atque corrupti quos dolores et quas molestias excepturi sint</p><div class="name">- MARA K.</div><div class="stars">★★★★★</div></div>
</section>

<!-- news -->
<section>
  <div class="eyebrow" style="top:2958px">Updates</div>
  <div class="section-title display" style="top:2990px">Latest News</div>
  <article class="news" style="left:100px"><div class="photo" role="img" aria-label="Hand testing a boiler control panel" style="background:linear-gradient(#8b8f93,#4d5257)"></div><div class="date">September 11,2021</div><h3>Lorem ipsum dolor sit amet, consectetur adipiscing</h3><p>Sed ut perspiciatis unde omnis iste natus error sit voluptatem accusantium doloremque laudantium, totam rem aperiam, eaque ipsa</p><div class="more">READ MORE ›</div></article>
  <article class="news" style="left:440px"><div class="photo" role="img" aria-label="Electrician in hard hat drilling a ceiling" style="background:linear-gradient(#b9b7ad,#6e6c5f)"></div><div class="date">September 11,2021</div><h3>Lorem ipsum dolor sit amet, consectetur adipiscing</h3><p>Sed ut perspiciatis unde omnis iste natus error sit voluptatem accusantium doloremque laudantium, totam rem aperiam, eaque ipsa</p><div class="more">READ MORE ›</div></article>
  <article class="news" style="left:780px"><div class="photo" role="img" aria-label="Electrician with tool belt at a wiring cabinet" style="background:linear-gradient(#c9c2bb,#6f6660)"></div><div class="date">September 11,2021</div><h3>Lorem ipsum dolor sit amet, consectetur adipiscing</h3><p>Sed ut perspiciatis unde omnis iste natus error sit voluptatem accusantium doloremque laudantium, totam rem aperiam, eaque ipsa</p><div class="more">READ MORE ›</div></article>
</section>

<!-- footer -->
<footer>
  <svg class="abs" style="left:0;top:3560px" width="1200" height="610" viewBox="0 0 1200 610">
    <path d="M0 110 Q600 -60 1200 110 L1200 610 L0 610 Z" fill="#111"/>
    <path d="M0 100 Q600 -70 1200 100" fill="none" stroke="#f4b400" stroke-width="5"/>
    <rect x="0" y="540" width="1200" height="70" fill="#1e1e1e"/>
  </svg>
  <div class="abs" style="left:530px;top:3602px;width:140px;height:140px;border-radius:50%;border:4px solid var(--white)"></div>
  <div class="abs" style="left:0;top:3742px;width:1200px;text-align:center;font-size:21px;font-weight:500;color:var(--white)">DORRISH ELECTRIC Ltd</div>
  <div class="footer-title display">Subscribe to our Newsletter</div>
  <div class="abs" style="left:125px;top:3826px;width:75px;height:3px;background:var(--yellow)"></div>
  <p class="abs" style="left:125px;top:3852px;width:490px;font-size:13px;line-height:19px;color:var(--white)">Enter your email and ge the very latest news from The Dorrish Circuit: tips and insights, announcements, events, and more! Sign up now!</p>
  <div class="field" style="top:3910px">Email</div>
  <div class="field" style="top:3967px">Phone</div>
  <div class="abs" style="left:125px;top:4026px;width:11px;height:11px;background:var(--white)"></div>
  <svg class="abs" style="left:126px;top:4027px" width="10" height="10"><path d="M1 5l3 3 5-7" stroke="#111" stroke-width="1.6" fill="none"/></svg>
  <div class="abs" style="left:143px;top:4024px;font-size:11px;color:var(--white)">Send me news and updates</div>
  <div class="btn" style="left:485px;top:4027px;width:117px;height:43px">Submit</div>
  <div class="abs" style="left:668px;top:3790px;width:1px;height:280px;background:#444"></div>
  <div class="foot-head" style="top:3793px">About</div>
  <div class="foot-text" style="top:3815px;width:390px;font-size:13.5px">At vero eos et accusamus et iusto odio dignissimos ducimus qui blanditiis praesentium voluptatum deleniti</div>
  <div class="foot-head" style="top:3898px">Contact Us</div>
  <svg class="abs" style="left:730px;top:3925px" width="12" height="90"><path d="M6 1a4 4 0 0 1 4 4c0 3-4 8-4 8s-4-5-4-8a4 4 0 0 1 4-4z" fill="#fff"/><circle cx="6" cy="33" r="5" fill="none" stroke="#fff" stroke-width="1.5"/><path d="M6 30v3h2" stroke="#fff" stroke-width="1.2" fill="none"/><path d="M2 55l3 0 1 2.5-1.5 1a6 6 0 0 0 3 3l1-1.5 2.5 1v3a1 1 0 0 1-1 1 9 9 0 0 1-9-9 1 1 0 0 1 1-1z" fill="#fff"/></svg>
  <div class="foot-text" style="left:750px;top:3918px;font-size:14px">48 Cedar Lane Harbourview BC 00000<br>Mon-Fri 08:00 AM - 05:00 PM<br>(555) 014-2290</div>
  <div class="social" style="left:730px"></div>
  <div class="social" style="left:774px"></div>
  <div class="social" style="left:818px"></div>
  <div class="social" style="left:862px"></div>
  <div class="social" style="left:906px"></div>
  <div class="social" style="left:950px"></div>
  <div class="social" style="left:994px"></div>
  <div class="abs" style="left:0;top:4124px;width:1200px;text-align:center;font-size:13px;color:var(--white)">Copyright © 2022 Dorrish Electric Ltd .All rights reserved.</div>
</footer>

</body>
</html>
```